KTR Sponsorship Packet Cover Design for Upcoming Gala

We need a design for our annual balls sponsorship package front and back cover, it must be a standard 8.5x11 in size. The design must capture the essence of the theme of the event, which is Paradise Valley, as well as be of the same qualities as years past (I've attached a sample that we do not want to go with, as well as last year's package for your review).

The Theme: Paradise Valley was the business district and entertainment center of a densely-populated African-American residential area in Detroit, Mi. It became known as a lively area with jazz bars and nightclubs. From the 1930s to the 1950s, residents in Black Bottom made significant contributions to American music, including blues, Big Band, and jazz.

The organization logos area also attached.

Target Market(s)

Corporate Sponsors - People in the legal community in Detroit, MI

Industry/Entity Type

Legal

Font styles to use
Decorative

Requirements
Must have
• Logo - Be reflective of the theme
Nice to have
• Past designs have generally used black quite a bit. We may want to stick with black, but accent colors may vary. The initial suggestion was red.

```html
<!DOCTYPE html>
<html lang="en">
<head>
<meta charset="utf-8">
<title>Barrister's Ball Sponsorship Package Cover</title>
<link rel="stylesheet" href="https://fonts.googleapis.com/css2?family=Abril+Fatface&family=Questrial&display=swap">
<style>
  :root {
    --ink: #03060d;
    --paper: #ffffff;
    --ember: #e8431c;
    --ember-deep: #a92a10;
    --divider: #c9502c;
  }
  html, body {
    margin: 0;
    padding: 0;
    width: 1200px;
    height: 776px;
    overflow: hidden;
    background: var(--ink);
  }
  p, h1 { margin: 0; }
  .spread {
    position: relative;
    width: 1200px;
    height: 776px;
    background: var(--ink);
    color: var(--paper);
    font-family: "Questrial", "Helvetica Neue", Arial, sans-serif;
  }
  .panel {
    position: absolute;
    top: 0;
    height: 776px;
  }
  .panel--back { left: 0; width: 600px; }
  .panel--front { left: 601px; width: 599px; }
  .fold {
    position: absolute;
    left: 600px;
    top: 0;
    width: 1px;
    height: 776px;
    background: var(--divider);
  }

  /* Back cover */
  .drip-bands {
    position: absolute;
    left: 212px;
    top: 0;
    width: 184px;
    height: 126px;
  }
  .contact {
    position: absolute;
    left: 0;
    width: 600px;
    text-align: center;
    font-size: 12px;
    letter-spacing: 3.7px;
    line-height: 17px;
    text-transform: uppercase;
  }
  .contact--address { top: 366px; }
  .contact--online { top: 416px; }
  .hotel-note {
    position: absolute;
    left: 139px;
    top: 732px;
    font-size: 8.5px;
    letter-spacing: 3.7px;
    line-height: 11px;
    text-transform: uppercase;
  }
  .org-mark {
    position: absolute;
    display: flex;
    align-items: center;
    gap: 5px;
    font-size: 15px;
    letter-spacing: 1px;
    color: var(--paper);
  }
  .org-mark__dot {
    width: 12px;
    height: 12px;
    border-radius: 50%;
    background: var(--paper);
  }
  .panel--back .org-mark { left: 24px; top: 732px; }
  .panel--front .org-mark { left: 492px; top: 732px; }

  /* Front cover */
  .title {
    position: absolute;
    left: 57px;
    top: 16px;
    font-family: "Abril Fatface", "Playfair Display", Georgia, serif;
    font-weight: 400;
    line-height: 1;
  }
  .title__line--top { display: block; font-size: 51px; letter-spacing: 0.3px; }
  .title__line--big { display: block; font-size: 76px; margin-top: -6px; }
  .subtitle {
    position: absolute;
    left: 57px;
    top: 146px;
    font-size: 17px;
    letter-spacing: 6.4px;
    text-transform: uppercase;
  }
  .event-date {
    position: absolute;
    left: 57px;
    top: 166px;
    font-family: "Abril Fatface", "Playfair Display", Georgia, serif;
    font-size: 52px;
    line-height: 1.1;
  }
  .hero {
    position: absolute;
    left: 44px;
    top: 240px;
    width: 380px;
    height: 500px;
  }
  .venue {
    position: absolute;
    left: 57px;
    top: 744px;
    font-size: 12px;
    letter-spacing: 5.9px;
    text-transform: uppercase;
    white-space: nowrap;
  }
</style>
</head>
<body>
<main class="spread">
  <section class="panel panel--back" aria-label="Back cover">
    <svg class="drip-bands" viewBox="0 0 184 126" aria-hidden="true">
      <rect x="0" y="0" width="184" height="61" fill="var(--ember)"/>
      <rect x="10" y="0" width="2" height="61" fill="var(--ink)"/>
      <rect x="25" y="0" width="2" height="61" fill="var(--ink)"/>
      <rect x="112" y="0" width="6" height="61" fill="var(--ink)"/>
      <rect x="155" y="0" width="3" height="61" fill="var(--ink)"/>
      <rect x="9" y="61" width="2" height="64" fill="var(--ember)"/>
      <rect x="22" y="61" width="2" height="64" fill="var(--ember)"/>
      <rect x="53" y="61" width="3" height="64" fill="var(--ember)"/>
      <rect x="86" y="61" width="5" height="18" fill="var(--ember)"/>
      <rect x="108" y="61" width="6" height="64" fill="var(--ember)"/>
      <rect x="142" y="61" width="4" height="20" fill="var(--ember)"/>
      <rect x="155" y="61" width="13" height="64" fill="var(--ember)"/>
    </svg>
    <p class="contact contact--address">210 Calder Avenue, Suite 400,<br>Detroit, MI 48201</p>
    <p class="contact contact--online">Email : ktrbarristersball@mailbox.org<br>Website : www.ktrbar.org</p>
    <div class="org-mark"><span class="org-mark__dot"></span><span>KTR</span></div>
    <p class="hotel-note">To book your hotel reservation visit:<br>TBD https:reserve.staylink.net/go/ktrball2023 TBD</p>
  </section>

  <div class="fold"></div>

  <section class="panel panel--front" aria-label="Front cover">
    <h1 class="title">
      <span class="title__line--top">BARRISTER'S</span>
      <span class="title__line--big">BALL</span>
    </h1>
    <p class="subtitle">Sponsorship Package</p>
    <p class="event-date">04.29.23</p>
    <svg class="hero" viewBox="0 0 380 500">
      <defs>
        <radialGradient id="glow" cx="0.5" cy="0.55" r="0.55">
          <stop offset="0" stop-color="var(--ember)"/>
          <stop offset="0.45" stop-color="var(--ember-deep)"/>
          <stop offset="1" stop-color="var(--ink)"/>
        </radialGradient>
      </defs>
      <rect x="0" y="0" width="376" height="330" fill="url(#glow)" role="img" aria-label="Illustration of a red hand holding a white line-drawn saxophone, a jazz nod to Paradise Valley"/>
      <g fill="var(--ember)" aria-hidden="true">
        <rect x="10" y="158" width="17" height="338"/>
        <rect x="32" y="190" width="22" height="306"/>
        <rect x="59" y="220" width="34" height="276"/>
        <rect x="99" y="360" width="14" height="136"/>
        <rect x="118" y="280" width="107" height="216"/>
        <rect x="230" y="350" width="88" height="146"/>
        <rect x="347" y="310" width="29" height="186"/>
      </g>
    </svg>
    <p class="venue">Riverside Grand Hotel Center</p>
    <div class="org-mark"><span class="org-mark__dot"></span><span>KTR</span></div>
  </section>
</main>
</body>
</html>
```